ONE Unique Graphic of (A real estate sales funnel)

I’m looking for someone to create a very simple but effective graphic representation of this drawing to represent my real estate sales funnel I am using this graphic to explain to real estate agents what a sales funnel is and does.

For more information check out my webpage

http://www.brightquillinstitute.com/welcome

I am still working on but most of the information you need is there this is not a live page but I am currently working on finishing it this weekend. The website should give you an idea of my colors and I like things clean and simple less is more

Deliverabel: ONE GRAPHIC, simple transparent background and with top label "Real Estate Sales Funnel"

```html
<!DOCTYPE html>
<html lang="en">
<head>
<meta charset="utf-8">
<title>Real Estate Sales Funnel</title>
<link rel="stylesheet" href="https://fonts.googleapis.com/css2?family=Montserrat:wght@500;600;700&display=swap">
<style>
  :root {
    --green-deep: #0e6e35;
    --green-dark: #15803f;
    --green-mid: #1f9a4a;
    --green-soft: #6ab245;
    --green-lime: #93bd3c;
    --title: #1a7a3a;
    --label: #3d3d3d;
    --line: #c9c9c9;
    --chip: #f2f2f2;
    --white: #ffffff;
  }
  html, body {
    margin: 0;
    padding: 0;
    width: 1130px;
    height: 1200px;
    overflow: hidden;
    background: var(--white);
  }
  .funnel-graphic {
    display: block;
    width: 1130px;
    height: 1200px;
    font-family: "Montserrat", sans-serif;
  }
  .title { fill: var(--title); font-size: 31px; font-weight: 700; letter-spacing: 6px; }
  .stage-label { fill: var(--label); font-size: 16px; font-weight: 500; letter-spacing: 3.5px; }
  .band-label { fill: var(--white); font-size: 16px; font-weight: 600; letter-spacing: 3.5px; }
  .channel-chip { fill: var(--chip); }
  .channel-name { fill: var(--label); font-size: 9.5px; font-weight: 600; }
  .connector { stroke: var(--line); stroke-width: 2; fill: none; }
  .arrow { stroke: var(--label); stroke-width: 1.6; fill: none; }
  .glyph { stroke: var(--white); stroke-width: 2.4; fill: none; stroke-linecap: round; stroke-linejoin: round; }
  .glyph-fill { fill: var(--white); }
  .money { fill: var(--white); font-size: 15px; font-weight: 600; letter-spacing: 1px; }
  .dark-glyph { stroke: #1f7a3e; stroke-width: 2.4; fill: none; stroke-linecap: round; stroke-linejoin: round; }
</style>
</head>
<body>
<svg class="funnel-graphic" viewBox="0 0 900 970" preserveAspectRatio="xMidYMid meet" role="img" aria-label="Real estate sales funnel">
  <defs>
    <filter id="soft-shadow" x="-30%" y="-30%" width="160%" height="160%">
      <feDropShadow dx="0" dy="3" stdDeviation="3" flood-color="#000" flood-opacity="0.18"/>
    </filter>
  </defs>

  <text class="title" x="458" y="70" text-anchor="middle">REAL ESTATE SALES FUNNEL</text>

  <!-- channel row -->
  <g class="channels">
    <path class="connector" d="M380 177 V188 H775 V177 M460 177 V188 M538 177 V188 M616 177 V188 M697 177 V188 M578 188 V205"/>
    <g filter="url(#soft-shadow)">
      <circle class="channel-chip" cx="380" cy="147" r="30"/>
      <circle class="channel-chip" cx="460" cy="147" r="30"/>
      <circle class="channel-chip" cx="538" cy="147" r="30"/>
      <circle class="channel-chip" cx="616" cy="147" r="30"/>
      <circle class="channel-chip" cx="697" cy="147" r="30"/>
      <circle class="channel-chip" cx="775" cy="147" r="30"/>
    </g>
    <text class="channel-name" x="380" y="150" text-anchor="middle">Vidora</text>
    <g class="feed-icon">
      <circle cx="450" cy="158" r="2.6" fill="#1f7a3e"/>
      <path class="dark-glyph" d="M450 146 a12 12 0 0 1 12 12 M450 138 a20 20 0 0 1 20 20"/>
    </g>
    <text class="channel-name" x="538" y="150" text-anchor="middle">Circlr</text>
    <g class="page-icon">
      <rect x="601" y="134" width="30" height="26" rx="2" class="dark-glyph"/>
      <path class="dark-glyph" d="M601 141 H631 M606 147 H616 M606 153 H616 M620 147 H626 V154 H620 Z"/>
    </g>
    <text class="channel-name" x="697" y="150" text-anchor="middle">Vidora</text>
    <text class="channel-name" x="775" y="150" text-anchor="middle">Pictura</text>
  </g>

  <!-- funnel bands, drawn bottom to top -->
  <g class="funnel" filter="url(#soft-shadow)">
    <path fill="var(--green-lime)" d="M478 600 L520 720 A54 10 0 0 0 628 720 L668 600 Z"/>
    <path fill="var(--green-soft)" d="M430 485 L478 605 A95 15 0 0 0 668 605 L715 485 Z"/>
    <path fill="var(--green-mid)" d="M378 355 L430 490 A142 18 0 0 0 715 490 L768 355 Z"/>
    <path fill="var(--green-dark)" d="M327 250 L378 360 A195 22 0 0 0 768 360 L817 250 Z"/>
    <ellipse fill="var(--green-deep)" cx="572" cy="250" rx="245" ry="42"/>
  </g>
  <text class="band-label" x="574" y="360" text-anchor="middle">LEAD CAPTURE</text>
  <text class="band-label" x="574" y="458" text-anchor="middle">CUSTOMER JOURNEY</text>
  <text class="band-label" x="574" y="574" text-anchor="middle">CONVERSATION</text>
  <text class="band-label" x="574" y="682" text-anchor="middle">BUY / SELL</text>

  <!-- stage markers -->
  <g class="stages">
    <circle cx="123" cy="328" r="44" fill="var(--green-deep)"/>
    <g class="glyph">
      <path d="M100 312 H146 L128 330 V345 L118 350 V330 Z"/>
      <circle cx="112" cy="304" r="3"/><circle cx="122" cy="300" r="3"/><circle cx="132" cy="304" r="3"/>
    </g>
    <circle cx="123" cy="353" r="8" class="glyph"/>
    <text class="stage-label" x="190" y="333">LEADS</text>
    <path class="arrow" d="M310 327 H342 M335 322 L342 327 L335 332"/>

    <circle cx="152" cy="437" r="44" fill="var(--green-mid)"/>
    <g class="glyph">
      <circle cx="158" cy="430" r="14" stroke-width="4"/>
      <path d="M148 441 L134 456" stroke-width="6"/>
    </g>
    <text class="stage-label" x="218" y="451">PROSPECTS</text>
    <path class="arrow" d="M362 444 H393 M386 439 L393 444 L386 449"/>

    <circle cx="173" cy="560" r="44" fill="var(--green-soft)"/>
    <g class="glyph-fill">
      <circle cx="158" cy="548" r="7"/><circle cx="188" cy="548" r="7"/><circle cx="173" cy="552" r="8"/>
      <path d="M145 578 a13 12 0 0 1 26 -8 V578 Z M201 578 a13 12 0 0 0 -26 -8 V578 Z M160 580 a13 14 0 0 1 26 0 Z"/>
    </g>
    <text class="stage-label" x="241" y="567">CUSTOMERS</text>
    <path class="arrow" d="M401 561 H432 M425 556 L432 561 L425 566"/>

    <circle cx="201" cy="670" r="44" fill="var(--green-lime)"/>
    <g class="glyph">
      <path d="M172 662 L184 656 L200 662 L218 656 L230 662"/>
      <path d="M182 668 L196 682 a4 4 0 0 0 6 -5 M192 686 a4 4 0 0 0 6 -5 L200 670 L212 666 L222 676 L206 690"/>
    </g>
    <text class="stage-label" x="278" y="680">CLIENTS</text>
    <path class="arrow" d="M453 674 H485 M478 669 L485 674 L478 679"/>
  </g>

  <!-- outcomes -->
  <g class="outcomes">
    <path class="connector" d="M568 728 V853 M568 745 H503 V767 M611 730 V778 M611 752 H662 V873"/>
    <circle cx="503" cy="797" r="30" fill="var(--green-lime)"/>
    <path class="glyph" d="M488 798 L503 784 L518 798 M492 794 V812 H514 V794 M500 812 V803 H506 V812"/>
    <circle cx="611" cy="808" r="30" fill="var(--green-soft)"/>
    <text class="money" x="611" y="813" text-anchor="middle">$$$</text>
    <circle cx="568" cy="883" r="30" fill="var(--green-mid)"/>
    <text class="money" x="568" y="888" text-anchor="middle">$$$</text>
    <circle cx="662" cy="903" r="30" fill="var(--green-deep)"/>
    <path class="glyph" d="M647 904 L662 890 L677 904 M651 900 V918 H673 V900 M659 918 V909 H665 V918"/>
  </g>
</svg>
</body>
</html>
```